FotoVELD buisnesscard

Hey :) I need a modern buisnesscard for my company FotoVELD
It most have:
Dagligleder og Fotograf: Eirik Tobias Vangsnes

Mob: +4791642508
Epost: post@fotoveld-eks.no
Adresse: Bjørkeveien22, 6099 Fjordvik

Facbook and instagram logo with text FotoVELD

FotoVELD logo

It Company

```html
<!DOCTYPE html>
<html lang="no">
<head>
<meta charset="utf-8">
<title>FotoVELD – visittkort</title>
<link href="https://fonts.googleapis.com/css2?family=Roboto:wght@400;700&display=swap" rel="stylesheet">
<style>
  :root{
    --backdrop:#2c2b30;
    --card:#e4e4e4;
    --ink:#2e2e30;
    --muted:#8c8c8e;
    --mark:#a3a3a5;
    --rule:#3a3a3c;
  }
  *{margin:0;padding:0;box-sizing:border-box}
  html,body{width:1200px;height:1050px;overflow:hidden}
  body{background:var(--backdrop);font-family:"Roboto",Arial,sans-serif;position:relative}
  .card{
    position:absolute;top:356px;width:520px;height:338px;
    background:var(--card);overflow:hidden;
  }
  .card--front{left:50px}
  .card--back{left:630px;display:flex;align-items:center;justify-content:center}

  .holder{position:absolute;left:34px;top:30px;width:220px}
  .holder__name{font-weight:700;font-size:26px;line-height:1.1;color:var(--ink)}
  .holder__role{
    margin-top:8px;padding-bottom:8px;font-size:10.5px;font-weight:700;
    letter-spacing:.4px;text-transform:uppercase;color:var(--muted);
    border-bottom:2px solid var(--rule);
  }
  .contact{list-style:none;margin-top:12px}
  .contact__item{display:flex;gap:12px;align-items:flex-start;font-size:13px;line-height:1.35;color:var(--muted);margin-bottom:6px}
  .contact__icon{width:13px;height:13px;flex:none;margin-top:2px;fill:none;stroke:var(--ink);stroke-width:1.6}

  .social{position:absolute;right:32px;top:38px;display:flex;align-items:center;gap:8px;font-size:13px;color:var(--muted)}
  .social__dot{width:10px;height:10px;border-radius:50%;background:var(--ink)}

  .brand-large{
    position:absolute;right:26px;bottom:26px;
    font-size:72px;font-weight:700;color:var(--mark);line-height:1;white-space:nowrap;
  }
  .brand-back{font-size:80px;font-weight:700;color:var(--mark);line-height:1;white-space:nowrap}
</style>
</head>
<body>
  <section class="card card--front" aria-label="Visittkort forside">
    <div class="holder">
      <h1 class="holder__name">Eirik Tobias Vangsnes</h1>
      <p class="holder__role">Daglig leder og fotograf</p>
      <ul class="contact">
        <li class="contact__item">
          <svg class="contact__icon" viewBox="0 0 14 14"><path d="M3 1l2.5 3-1.5 1.5c.8 1.8 2.2 3.2 4 4L9.5 8l3 2.5-1.5 2.5C6 13 1 8 1 3z"/></svg>
          <span>+4791642508</span>
        </li>
        <li class="contact__item">
          <svg class="contact__icon" viewBox="0 0 14 14"><rect x="1" y="3" width="12" height="8"/><path d="M1 3l6 5 6-5"/></svg>
          <span>post@fotoveld-eks.no</span>
        </li>
        <li class="contact__item">
          <svg class="contact__icon" viewBox="0 0 14 14"><path d="M7 13s-4.5-4.5-4.5-7.5a4.5 4.5 0 019 0C11.5 8.5 7 13 7 13z"/><circle cx="7" cy="5.5" r="1.5"/></svg>
          <span>Bjørkeveien22<br>6099 Fjordvik</span>
        </li>
      </ul>
    </div>
    <div class="social"><span class="social__dot"></span><span>FotoVELD</span></div>
    <div class="brand-large">FotoVELD</div>
  </section>

  <section class="card card--back" aria-label="Visittkort bakside">
    <div class="brand-back">FotoVELD</div>
  </section>
</body>
</html>
```